Flyer overhaul from current flyers

I need to have our current flyers updated with a fresher look. We also need to have a new utility and real estate flyer created that will go along with the design of the new flyer. We are looking for new pictures, new overall design, same color scheme but would like to have the flyers more airy and inviting.

Target Market(s)

decision makers in the healthcare/utilty/banking/real estate sectors

Font styles to use
Other font styles liked:
• Logo is in Bell MT

Colors
0054AA
0677BA
7BADD7
CADEEF
E8F1F8

Requirements
Must have
• Close to what is currently on the existing flyers

```html
<!DOCTYPE html>
<html lang="en">
<head>
<meta charset="utf-8">
<title>Riverbend Recovery Flyers</title>
<link rel="stylesheet" href="https://fonts.googleapis.com/css2?family=Roboto:wght@400;500;700&family=Roboto+Slab:wght@700&display=swap">
<style>
  :root {
    --stage: #898a8c;
    --band: rgba(66, 74, 78, 0.88);
    --bar: #4a5256;
    --accent: #18a4dc;
    --banner: #4aa2c4;
    --white: #ffffff;
    --deep-top: #2f8db1;
    --deep-mid: #187399;
    --deep-low: #1d5a79;
    --photo-a: #c9d6dc;
    --photo-b: #7fa9bd;
    --photo-c: #b7b9d6;
    --photo-d: #8fb4d2;
  }
  * { margin: 0; padding: 0; box-sizing: border-box; }
  html, body { width: 1200px; height: 841px; overflow: hidden; }
  body { background: var(--stage); font-family: "Roboto", Arial, sans-serif; color: var(--white); position: relative; }

  .flyer { position: absolute; width: 497px; height: 645px; overflow: hidden;
    background: linear-gradient(180deg, var(--deep-top) 0%, var(--deep-top) 42%, var(--deep-mid) 62%, var(--deep-low) 100%); }
  .flyer--services { left: 83px; top: 73px; }
  .flyer--philosophy { left: 637px; top: 74px; }

  .photo { position: absolute; left: 0; top: 0; width: 100%; }
  .flyer--services .photo { height: 330px;
    background: linear-gradient(180deg, var(--photo-a) 0%, #a9c3cf 35%, var(--photo-b) 65%, rgba(47,141,177,0) 100%); }
  .flyer--philosophy .photo { height: 350px;
    background: linear-gradient(180deg, var(--photo-c) 0%, #c6cbe0 30%, var(--photo-d) 70%, rgba(47,141,177,0) 100%); }

  .brand-band { position: absolute; left: 0; top: 24px; width: 370px; height: 81px; background: var(--band);
    display: flex; align-items: center; padding-left: 29px; gap: 10px; }
  .flyer--philosophy .brand-band { top: 26px; }
  .brand-dot { width: 60px; height: 60px; border-radius: 50%; background: var(--white); flex: none; }
  .brand-name { font-size: 21px; font-weight: 400; line-height: 1.05; letter-spacing: 1px; text-transform: uppercase; }

  .headline { position: absolute; left: 28px; top: 112px; font-size: 55px; font-weight: 700; line-height: 50px; letter-spacing: -0.5px; }

  .kicker { position: absolute; left: 43px; top: 272px; font-size: 19px; font-weight: 700; color: var(--accent); }
  .checklist { position: absolute; left: 43px; top: 306px; list-style: none; }
  .checklist li { font-size: 15px; line-height: 18.6px; display: flex; align-items: center; gap: 4px; }
  .checklist svg { width: 14px; height: 14px; flex: none; }

  .banner { position: absolute; left: 43px; top: 408px; width: 415px; height: 39px; background: var(--banner);
    font-size: 19px; font-weight: 700; display: flex; align-items: center; justify-content: center; }

  .service-list { position: absolute; top: 462px; list-style: none; }
  .service-list--a { left: 43px; }
  .service-list--b { left: 278px; }
  .service-list li { font-size: 12.5px; line-height: 14.6px; padding-left: 12px; position: relative; }
  .service-list li::before { content: ""; position: absolute; left: 0; top: 6px; width: 3px; height: 3px; border-radius: 50%; background: var(--white); }

  .section-title { position: absolute; left: 0; width: 100%; top: 334px; text-align: center; font-size: 35px; font-weight: 700; }
  .rule { position: absolute; left: 93px; width: 311px; top: 390px; height: 1px; background: var(--accent); }
  .story { position: absolute; left: 60px; width: 406px; top: 402px; font-size: 9.6px; line-height: 16px; text-align: justify; }

  .cta { position: absolute; left: 0; width: 100%; text-align: center; }
  .cta-label { top: 548px; font-size: 15px; font-weight: 700; }
  .cta-phone { top: 570px; font-size: 25px; font-weight: 700; }
  .flyer--philosophy .cta-label { top: 551px; }
  .flyer--philosophy .cta-phone { top: 573px; }
  .web-bar { position: absolute; left: 139px; width: 220px; bottom: 0; height: 28px; background: var(--bar);
    font-family: "Roboto Slab", Georgia, serif; font-weight: 700; font-size: 11.5px; display: flex; align-items: center; justify-content: center; }
</style>
</head>
<body>

<section class="flyer flyer--services">
  <div class="photo" role="img" aria-label="Photo of business people reviewing financial documents at a desk"></div>
  <div class="brand-band">
    <span class="brand-dot"></span>
    <span class="brand-name">Riverbend<br>Recovery</span>
  </div>
  <h1 class="headline">Financial<br>Collections</h1>
  <h2 class="kicker">A Forward Thinking Approach</h2>
  <ul class="checklist">
    <li><svg viewBox="0 0 14 14"><path d="M1 8 L5 12 L13 1" fill="none" stroke="#fff" stroke-width="1.8"/></svg>Consumer Friendly, Professional Approach</li>
    <li><svg viewBox="0 0 14 14"><path d="M1 8 L5 12 L13 1" fill="none" stroke="#fff" stroke-width="1.8"/></svg>Online Consumer Debt Negotiation Tools</li>
    <li><svg viewBox="0 0 14 14"><path d="M1 8 L5 12 L13 1" fill="none" stroke="#fff" stroke-width="1.8"/></svg>Live Online Agent Chat Portals</li>
    <li><svg viewBox="0 0 14 14"><path d="M1 8 L5 12 L13 1" fill="none" stroke="#fff" stroke-width="1.8"/></svg>Online Consumer Dispute/Complaint Tools</li>
    <li><svg viewBox="0 0 14 14"><path d="M1 8 L5 12 L13 1" fill="none" stroke="#fff" stroke-width="1.8"/></svg>FISMA Compliant Physical and Virtual Security</li>
  </ul>
  <div class="banner">An Impactful, All-In-One Solution</div>
  <ul class="service-list service-list--a">
    <li>Credit Report Monitoring</li>
    <li>Address/Phone Scrubbing</li>
    <li>Compliant Collection Letters</li>
    <li>Discretionary Credit Reporting</li>
    <li>Customizable Collection Workflow</li>
  </ul>
  <ul class="service-list service-list--b">
    <li>Professional Skip Tracing</li>
    <li>Deceased/Probate Services</li>
    <li>Call Recording and Monitoring</li>
    <li>Bankruptcy Claim Services</li>
    <li>Legal Collection Services</li>
  </ul>
  <p class="cta cta-label">CALL US AT</p>
  <p class="cta cta-phone">(555) 214-7300</p>
  <div class="web-bar">www.riverbendrecovery.com</div>
</section>

<section class="flyer flyer--philosophy">
  <div class="photo" role="img" aria-label="Photo of a hand with a pen using a calculator over rising bar charts"></div>
  <div class="brand-band">
    <span class="brand-dot"></span>
    <span class="brand-name">Riverbend<br>Recovery</span>
  </div>
  <h2 class="section-title">Our Philosophy</h2>
  <div class="rule"></div>
  <p class="story">For over 30 years, Riverbend Recovery has assisted banks and financial services companies in the reconciliation of their past due accounts. Our philosophy is to provide consistent performance by investing in our clients' accounts to ensure the maximum liquidation. By building on historically proven collection techniques and employing an ever-expanding access to data and technology, our agency has continued to improve our performance to the benefit of our clients. Our capital forward, compliance centered approach has proven to deliver the most consistent results for our financial service</p>
  <p class="cta cta-label">CALL US AT</p>
  <p class="cta cta-phone">(555) 214-7300</p>
  <div class="web-bar">www.riverbendrecovery.com</div>
</section>

</body>
</html>
```